Web app UI design

This web app has been built and the UI needs a refresh.

Attached are the pages which need the refresh.

The web app is for a cyber security product/service and customers are inputting their details.

```html
<!DOCTYPE html>
<html lang="en">
<head>
<meta charset="utf-8">
<title>Trustline – Welcome</title>
<link href="https://fonts.googleapis.com/css2?family=Inter:wght@300;400;500;600;700&display=swap" rel="stylesheet">
<style>
  :root{
    --page:#97a0ac;
    --shell:#1c202b;
    --divider:#272c38;
    --panel:#212736;
    --step:#262c3b;
    --blue:#2d66e8;
    --blue-bright:#3d7bf5;
    --blue-soft:#b9cdfb;
    --text:#ffffff;
    --muted:#8b93a5;
    --icon:#7d8596;
    --online:#22d45a;
  }
  *{box-sizing:border-box;margin:0;padding:0}
  html,body{width:1200px;height:790px;overflow:hidden}
  body{background:var(--page);font-family:"Inter",sans-serif;color:var(--text);position:relative}

  .app{position:absolute;left:93px;top:92px;width:1015px;height:606px;background:var(--shell);border-radius:22px;overflow:hidden;box-shadow:0 18px 40px rgba(40,48,62,.35)}
  .sidebar{position:absolute;left:0;top:0;width:86px;height:100%;border-right:1px solid var(--divider)}
  .menu-toggle{position:absolute;left:32px;top:33px}
  .nav-item{position:absolute;left:19px;width:45px;height:45px;border-radius:8px;display:flex;align-items:center;justify-content:center}
  .nav-item.active{background:var(--blue)}
  .avatar{position:absolute;left:29px;top:537px;width:28px;height:28px;border-radius:50%;background:linear-gradient(135deg,#8a6a58,#3b3430)}
  .avatar .status{position:absolute;right:-4px;top:2px;width:8px;height:8px;border-radius:50%;background:var(--online)}

  .brand{position:absolute;left:123px;top:28px;font-size:13.5px;font-weight:500;letter-spacing:.3px}

  .hero{position:absolute;left:122px;top:77px;width:842px;height:194px;background:var(--blue);border-radius:17px;overflow:hidden}
  .hero-photo{position:absolute;right:0;top:0;width:390px;height:100%;
    background:
      radial-gradient(circle at 62% 45%,rgba(150,220,255,.7) 0,rgba(90,150,240,.2) 12%,transparent 26%),
      linear-gradient(90deg,var(--blue) 0%,#2b56b8 22%,#5a6f9a 55%,#c9c4c2 78%,#e7e3e1 100%)}
  .hero-eyebrow{position:absolute;left:39px;top:30px;font-size:13.5px;font-weight:400;color:var(--blue-soft)}
  .hero-title{position:absolute;left:38px;top:53px;font-size:50px;font-weight:500;letter-spacing:-.5px;line-height:1}
  .hero-lead{position:absolute;left:39px;top:112px;font-size:13.5px;font-weight:700}
  .hero-note{position:absolute;left:39px;top:132px;font-size:9px;font-weight:400;color:var(--blue-soft)}

  .setup{position:absolute;left:122px;top:297px;width:842px;height:264px;background:var(--panel);border-radius:17px}
  .setup-title{position:absolute;left:39px;top:41px;font-size:18px;font-weight:500;color:var(--muted)}
  .setup-sub{position:absolute;left:39px;top:65px;font-size:9px;color:var(--muted)}

  .step{position:absolute;top:105px;width:122px;height:118px;background:var(--step);border-radius:12px;text-align:center}
  .step-icon{position:absolute;left:41px;top:19px;width:40px;height:40px}
  .step-label{position:absolute;left:0;right:0;top:69px;font-size:11.5px;font-weight:500;line-height:1.2}
  .step-label .accent{color:var(--blue-bright)}
  .step-label.plain{font-weight:400}
  .step-label.dim{color:#c7ccd6;font-weight:400}
  .step-hint{position:absolute;left:0;right:0;top:86px;font-size:7.5px;color:var(--muted);line-height:1.3}
  .step-arrow{position:absolute;top:161px}
</style>
</head>
<body>
<main class="app">
  <aside class="sidebar">
    <svg class="menu-toggle" width="24" height="9" viewBox="0 0 24 9"><path d="M0 1h24M0 8h14" stroke="#fff" stroke-width="1.4"/></svg>
    <a class="nav-item active" style="top:77px" aria-label="Home">
      <svg width="22" height="22" viewBox="0 0 24 24" fill="none" stroke="#fff" stroke-width="1.8" stroke-linejoin="round"><path d="M3 11 12 3l9 8v10h-6v-6H9v6H3z"/></svg>
    </a>
    <a class="nav-item" style="top:142px" aria-label="Profile">
      <svg width="24" height="24" viewBox="0 0 24 24" fill="none" stroke="var(--icon)" stroke-width="1.4"><circle cx="10" cy="7" r="4"/><path d="M3 21c0-4 3-7 7-7 2 0 3 .4 4 1"/><path d="M15 21l1-4 4-4 1.5 1.5-4 4z"/></svg>
    </a>
    <a class="nav-item" style="top:206px" aria-label="Subscription">
      <svg width="24" height="24" viewBox="0 0 24 24" fill="none" stroke="var(--icon)" stroke-width="1.4"><rect x="5" y="2" width="12" height="18" rx="2"/><path d="M10 22v-9a1.5 1.5 0 0 1 3 0v4l4 1v4"/></svg>
    </a>
    <a class="nav-item" style="top:272px" aria-label="Account status">
      <svg width="26" height="26" viewBox="0 0 26 26" fill="none" stroke="var(--icon)" stroke-width="1.4"><circle cx="10" cy="7" r="4"/><path d="M3 22c0-4 3-7 7-7 1.5 0 2.5.3 3.5.8"/><path d="m15 20 3 3 6-6"/></svg>
    </a>
    <div class="avatar" role="img" aria-label="User profile photo"><span class="status"></span></div>
  </aside>

  <div class="brand">TRUSTLINE</div>

  <section class="hero">
    <div class="hero-photo" role="img" aria-label="Photo of a person touching a glowing interface of security and data icons"></div>
    <p class="hero-eyebrow">Trustline</p>
    <h1 class="hero-title">Welcome</h1>
    <p class="hero-lead">Thank you signing up with Trustline.</p>
    <p class="hero-note">We are launching in a few weeks and will contact you shortly</p>
  </section>

  <section class="setup">
    <h2 class="setup-title">Setup Guide</h2>
    <p class="setup-sub">Please follow he below steps to get started</p>

    <div class="step" style="left:29px">
      <svg class="step-icon" viewBox="0 0 40 40" fill="none"><rect x="1" y="1" width="38" height="12" rx="5" stroke="#fff" stroke-width="1"/><text x="20" y="10" font-family="Inter,sans-serif" font-size="7" fill="#fff" text-anchor="middle">SIGN UP</text><path d="M17 39c-3-2-5-5-6-7l2-1 3 3V16a1.5 1.5 0 0 1 3 0v9m0-2a1.5 1.5 0 0 1 3 0v2m0-1a1.5 1.5 0 0 1 3 0v2m0-1a1.5 1.5 0 0 1 3 0v6c0 3-2 6-2 6" stroke="var(--blue-bright)" stroke-width="1.2"/></svg>
      <p class="step-label plain">Register Account</p>
    </div>
    <svg class="step-arrow" style="left:176px" width="8" height="12" viewBox="0 0 8 12"><path d="m1 1 5 5-5 5" stroke="#9aa1b0" stroke-width="1.2" fill="none"/></svg>

    <div class="step" style="left:193px">
      <svg class="step-icon" viewBox="0 0 40 40" fill="none"><path d="M6 31A19 19 0 1 1 20 39" stroke="#fff" stroke-width="1"/><path d="M3 29l3 2 2-3" stroke="#fff" stroke-width="1"/><circle cx="20" cy="15" r="4" stroke="var(--blue-bright)" stroke-width="1.2"/><path d="M12 27c0-4 4-6 8-6s8 2 8 6z" stroke="var(--blue-bright)" stroke-width="1.2"/></svg>
      <p class="step-label">Update <span class="accent">Profile</span></p>
      <p class="step-hint">Setup basic account info</p>
    </div>
    <svg class="step-arrow" style="left:337px" width="8" height="12" viewBox="0 0 8 12"><path d="m1 1 5 5-5 5" stroke="#9aa1b0" stroke-width="1.2" fill="none"/></svg>

    <div class="step" style="left:356px">
      <svg class="step-icon" viewBox="0 0 40 40" fill="none"><rect x="6" y="1" width="5" height="17" rx="2" stroke="#fff" stroke-width="1"/><path d="M14 18V3a2 2 0 0 1 2-2h3a2 2 0 0 1 2 2v3" stroke="#fff" stroke-width="1"/><path d="M25 39c-3-2-6-5-7-7l2-1 3 3V16a1.5 1.5 0 0 1 3 0v9m0-2a1.5 1.5 0 0 1 3 0v2m0-1a1.5 1.5 0 0 1 3 0v2m0-1a1.5 1.5 0 0 1 3 0v6c0 3-2 6-2 6" stroke="var(--blue-bright)" stroke-width="1.2"/></svg>
      <p class="step-label">Select <span class="accent">Subscription</span></p>
      <p class="step-hint">Select and setup<br>Subscription type</p>
    </div>
    <svg class="step-arrow" style="left:502px" width="8" height="12" viewBox="0 0 8 12"><path d="m1 1 5 5-5 5" stroke="#9aa1b0" stroke-width="1.2" fill="none"/></svg>

    <div class="step" style="left:520px">
      <svg class="step-icon" viewBox="0 0 40 40" fill="none"><path d="M24 4 15 0 1 5v12c0 9 7 15 14 19" stroke="#fff" stroke-width="1"/><rect x="20" y="18" width="19" height="16" rx="2" stroke="var(--blue-bright)" stroke-width="1.2"/><path d="M20 23h19M24 28h9M24 31h6" stroke="var(--blue-bright)" stroke-width="1.2"/></svg>
      <p class="step-label plain">Setup details<br>to protect</p>
    </div>
    <svg class="step-arrow" style="left:668px" width="8" height="12" viewBox="0 0 8 12"><path d="m1 1 5 5-5 5" stroke="#9aa1b0" stroke-width="1.2" fill="none"/></svg>

    <div class="step" style="left:684px">
      <svg class="step-icon" viewBox="0 0 40 40" fill="none"><circle cx="20" cy="20" r="19" stroke="#fff" stroke-width="1"/><circle cx="18" cy="14" r="3.5" stroke="var(--blue-bright)" stroke-width="1.2"/><path d="M11 26c0-4 3-6 7-6" stroke="var(--blue-bright)" stroke-width="1.2"/><path d="m19 25 3 3 7-7" stroke="#fff" stroke-width="1.2"/></svg>
      <p class="step-label dim">Account Active</p>
    </div>
  </section>
</main>
</body>
</html>
```